Banner Designs for Drone Defense Ad Campaign

Corvane is a security consulting and services company that offers a service called SkyMindful. SkyMindful helps our customers identify security risks from drones and develops comprehensive protection programs. We are looking for a designer to create a banner ad in three sizes for our campaign.
Target Market(s)
Our campaign is geared to the sports and entertainment industry, specifically large event venues and their security operation.
Industry/Entity Type
Security
Font styles to use
Other font styles liked:
- Raleway
Requirements
Must have
- Banner Objective
The visual and textual content of the banner should prompt the viewer to quickly identify the service offered and the information that is available to download.
Banner Design
Logo: SkyMindful logo
Call to Action Button in Red: Get It Here (On Right or or Upper Right)
Title in Larger Font: Guide to UAS Risk Mitigation
Subtitle in smaller Font: 5 Steps to Develop Your Comprehensive UAS Defense Program
Background: Stadium with a drone flying in foreground
Font: Raleway
Banner Sizes
1 - 1200x670 pixels
2 - 1510x196 pixels
3 - 1200x628 pixels

```html
<!DOCTYPE html>
<html lang="en">
<head>
<meta charset="utf-8">
<title>Guide to UAS Risk Mitigation – SkyMindful by Corvane</title>
<link rel="stylesheet" href="https://fonts.googleapis.com/css2?family=Raleway:wght@400;500;600;700;800;900&display=swap">
<style>
  :root {
    --ink-black: #000000;
    --night-blue: #0c2236;
    --stadium-deep: #0a1a26;
    --stadium-mid: #1d3a4e;
    --pitch-green: #23361f;
    --overlay-blue: rgba(40, 90, 130, 0.55);
    --text-white: #ffffff;
    --cta-red: #d3312b;
  }
  html, body {
    margin: 0;
    padding: 0;
    overflow: hidden;
    background: #ffffff;
  }
  .banner {
    position: relative;
    width: 1200px;
    height: 156px;
    overflow: hidden;
    font-family: "Raleway", sans-serif;
    color: var(--text-white);
    background: var(--stadium-deep);
  }
  .banner__photo {
    position: absolute;
    inset: 0;
    background:
      radial-gradient(ellipse 120px 70px at 850px 78px, rgba(200,210,220,0.35), transparent 70%),
      linear-gradient(180deg, var(--stadium-mid) 0%, var(--stadium-deep) 60%, var(--pitch-green) 100%);
  }
  .banner__shapes {
    position: absolute;
    inset: 0;
  }
  .brand {
    position: absolute;
    left: 41px;
    top: 64px;
    text-align: right;
    width: 126px;
  }
  .brand__name {
    display: block;
    font-weight: 700;
    font-size: 17px;
    letter-spacing: -0.2px;
    text-align: left;
    line-height: 1;
  }
  .brand__parent {
    display: block;
    font-weight: 500;
    font-size: 8px;
    margin-top: 4px;
    margin-right: 28px;
  }
  .headline {
    position: absolute;
    left: 306px;
    top: 28px;
  }
  .headline__title {
    margin: 0;
    font-weight: 900;
    font-size: 34px;
    line-height: 29px;
    letter-spacing: 0.2px;
    text-transform: uppercase;
  }
  .headline__subtitle {
    margin: 9px 0 0;
    font-weight: 500;
    font-size: 12.5px;
    line-height: 14px;
    text-transform: uppercase;
  }
  .cta {
    position: absolute;
    left: 1033px;
    top: 60px;
    width: 132px;
    height: 37px;
    background: var(--cta-red);
    color: var(--text-white);
    font-weight: 700;
    font-size: 15px;
    display: flex;
    align-items: center;
    justify-content: center;
    text-decoration: none;
    letter-spacing: -0.2px;
  }
</style>
</head>
<body>
  <div class="banner">
    <div class="banner__photo" role="img" aria-label="Packed stadium crowd at night with a white quadcopter drone flying in the foreground"></div>
    <svg class="banner__shapes" width="1200" height="156" viewBox="0 0 1200 156" aria-hidden="true">
      <polygon points="0,0 700,0 555,156 0,156" fill="var(--overlay-blue)"/>
      <polygon points="0,0 210,0 75,156 0,156" fill="var(--ink-black)"/>
    </svg>

    <div class="brand">
      <span class="brand__name">SkyMindful</span>
      <span class="brand__parent">By Corvane</span>
    </div>

    <div class="headline">
      <h1 class="headline__title">Guide to UAS<br>Risk Mitigation</h1>
      <p class="headline__subtitle">5 Steps to Develop Your Comprehensive<br>UAS Defense Program</p>
    </div>

    <a class="cta" href="#">GET IT HERE</a>
  </div>
</body>
</html>
```